Business Name: K&T Holdings Cleaning Services - Cleaning business

We need a website to be able to get our services out to the market..
We have just invested over $60,000 in our new van which is capable of doing specialised cleaning services see attached flyer... I will also send through our company logo....We do all types of cleaning from move out cleans, office cleans and have the capability fire flood and restoration services as well
On the flyer it has Gerald as a contact do not use his name only use Martin as a contact
Want some good pictures included
Prefer people to contact me via email rather than calling me.

```html
<!DOCTYPE html>
<html lang="en">
<head>
<meta charset="utf-8">
<title>K&amp;T Holdings Cleaning Services</title>
<link href="https://fonts.googleapis.com/css2?family=Open+Sans:ital,wght@0,400;0,600;0,700;0,800;1,400;1,600&display=swap" rel="stylesheet">
<style>
:root{
  --orange:#f7861e;
  --orange-dark:#e8731a;
  --ink:#1f2328;
  --text:#555b61;
  --muted:#8a9096;
  --sky:#eef6fa;
  --sky-deep:#dbe9f1;
  --line:#e3e8ec;
  --white:#ffffff;
}
*{margin:0;padding:0;box-sizing:border-box}
html,body{width:1200px;height:5014px;overflow:hidden}
body{font-family:"Open Sans",Arial,sans-serif;color:var(--text);background:var(--white);position:relative}
.section{position:absolute;left:0;width:1200px}
.abs{position:absolute}
.btn{display:inline-block;background:var(--orange);color:var(--white);font-weight:700;font-size:14px;letter-spacing:.5px;text-transform:uppercase;border-radius:22px;padding:11px 26px}
.title{font-weight:800;color:var(--ink);text-align:center;font-size:32px}
.lead{text-align:center;font-size:14px;line-height:1.55;color:var(--text)}
.spark{display:block;margin:0 auto 10px}
.photo{border-radius:2px}

/* header + hero */
.hero{top:0;height:620px;background:var(--sky)}
.topbar{top:6px;right:86px;font-size:11px;color:var(--text);display:flex;gap:22px}
.logo{top:0;left:84px;width:120px;height:130px;background:var(--white);display:flex;flex-direction:column;align-items:center;justify-content:center;gap:6px}
.logo-mark{width:44px;height:44px;border-radius:50%;background:var(--orange)}
.logo-name{font-weight:800;font-size:14px;color:var(--orange);text-align:center;line-height:1.2}
.nav{top:42px;left:418px;display:flex;align-items:center;gap:34px;font-size:13px;font-weight:600;color:var(--ink);text-transform:uppercase}
.nav .active{color:var(--orange);border-bottom:2px solid var(--orange);padding-bottom:6px}
.nav .btn{font-size:13px;padding:9px 20px}
.hero-title{top:212px;left:84px;font-size:56px;font-weight:800;color:var(--ink);line-height:1.3}
.hero-title span{color:var(--orange)}
.hero-sub{top:378px;left:86px;font-size:15px;color:var(--ink)}
.hero-btn{top:420px;left:84px}
.hero-art{top:110px;left:640px;width:320px;height:500px;border-radius:18px;background:linear-gradient(180deg,#f6e6d6 0%,#cfe0f0 45%,#7fa6d8 100%);opacity:.9}
.hero-plant{top:150px;left:1000px;width:140px;height:320px;border-radius:18px;background:linear-gradient(180deg,#d6ebbd,#9cc76f)}

/* goal */
.goal{top:680px;height:480px}
.goal-photo{top:22px;left:84px;width:500px;height:435px;background:linear-gradient(135deg,#f3ede3 0%,#c69a62 55%,#8a5a2c 100%)}
.goal-text{top:18px;left:612px;width:500px}
.goal-text h2{font-size:28px;font-weight:800;color:var(--ink);line-height:1.25;margin-bottom:8px}
.goal-text p{font-size:13.5px;line-height:1.55}
.goal-text h3{font-size:21px;font-weight:700;color:var(--orange);margin:14px 0 4px;display:flex;align-items:center;gap:8px}
.goal-text h3::before{content:"";width:11px;height:11px;border:3px solid var(--orange);border-radius:50%}
.goal-text .btn{margin-top:22px}

/* reasons */
.reasons{top:1250px;height:560px;background-image:radial-gradient(#e8edf0 1px,transparent 1.5px);background-size:14px 14px}
.reasons .head{top:80px;left:0;width:1200px}
.reasons .lead{width:820px;margin:10px auto 0}
.features{top:240px;left:84px;width:1032px;display:flex;justify-content:space-between}
.feature{width:240px;text-align:center}
.feature .icon{width:78px;height:78px;margin:0 auto 14px;background:var(--sky);display:flex;align-items:center;justify-content:center}
.feature h4{font-size:20px;font-weight:700;color:var(--orange);line-height:1.25}
.feature h4 small{display:block;font-size:18px;font-weight:400}
.feature p{font-size:13px;line-height:1.55;margin-top:18px}

/* testimonial */
.clients{top:1910px;height:240px}
.quote-mark{top:20px;left:84px;font-size:210px;font-weight:800;color:var(--sky);line-height:1}
.clients h2{top:58px;left:150px;font-size:34px;font-weight:700;color:var(--ink);line-height:1.2}
.avatar{top:22px;left:445px;width:84px;height:84px;border-radius:50%;background:linear-gradient(180deg,#6b4a38,#c9a58a)}
.quote{top:118px;left:426px;width:580px;font-size:14.5px;line-height:1.6;color:var(--ink)}
.author{top:210px;left:426px;font-size:14px;font-weight:700;font-style:italic;color:var(--ink)}

/* how it works */
.works{top:2225px;height:540px;background:var(--sky)}
.works .head{top:70px;left:0;width:1200px}
.works .lead{width:820px;margin:10px auto 0}
.step{top:245px;width:360px;text-align:center}
.step .num{width:132px;height:132px;border-radius:50%;background:var(--white);margin:0 auto;display:flex;align-items:center;justify-content:center;font-size:54px;font-weight:700;color:var(--ink)}
.step h4{margin-top:22px;font-size:21px;font-weight:700;color:var(--orange)}
.step p{font-size:20px;color:var(--ink);margin-top:6px}
.connector{top:305px}

/* news */
.news{top:2840px;height:760px}
.news .head{top:40px;left:0;width:1200px}
.news .lead{width:820px;margin:10px auto 0}
.card{top:162px;width:327px}
.card .photo{height:242px}
.card h3{font-size:21px;font-weight:800;color:var(--ink);line-height:1.3;margin-top:24px}
.card .date{font-size:12px;color:var(--muted);margin-top:12px;display:flex;align-items:center;gap:6px}
.card p{font-size:12.5px;line-height:1.55;color:var(--ink);margin-top:10px}
.card .more{display:inline-block;margin-top:14px;font-size:12px;font-weight:700;color:var(--orange);text-transform:uppercase;border-bottom:1px solid var(--orange)}

/* offer band */
.offer{top:3604px;height:268px;background:linear-gradient(90deg,#e6eef2,#f4f7f8 45%,#e4ecef);text-align:center}
.offer h2{margin-top:66px;font-size:42px;font-weight:800;color:var(--ink)}
.offer h2 span{color:var(--orange)}
.offer p{font-size:16px;color:var(--ink);margin-top:6px}
.offer .until{font-weight:600}
.offer .until span{color:var(--orange)}

/* estimates */
.estimate{top:3925px;height:520px}
.estimate-text{top:28px;left:84px;width:470px}
.estimate-text h2{font-size:31px;font-weight:700;color:var(--ink);line-height:1.25}
.estimate-text h4{font-size:19px;font-weight:700;color:var(--ink);margin:10px 0 14px}
.estimate-text p{font-size:13.5px;line-height:1.6;margin-bottom:26px}
.tile{width:240px;height:178px}
.tile-label{background:var(--orange);display:flex;align-items:center;justify-content:center;text-align:center;color:var(--white);font-weight:700;font-size:20px;line-height:1.3;text-transform:uppercase;outline:2px solid rgba(255,255,255,.7);outline-offset:-22px}

/* footer */
.footer{top:4478px;height:474px;background:var(--sky)}
.col h5{font-size:18px;font-weight:800;color:var(--ink);text-transform:uppercase;border-bottom:1px solid var(--line);padding-bottom:10px;margin-bottom:16px;width:210px}
.col p{font-size:13px;line-height:1.6}
.col ul{list-style:none;font-size:14px;line-height:1.8;color:var(--text)}
.col li::before{content:"– ";color:var(--orange)}
.badges{display:flex;gap:12px;margin-top:18px}
.badge{width:42px;height:42px;border-radius:50%;background:#c5cdd3}
.col .tagline{font-size:32px;font-weight:800;color:var(--ink);line-height:1.2;margin-top:18px}
.subscribe{top:82px;left:876px;width:236px;height:278px;background:var(--white);text-align:center;padding:28px 20px}
.subscribe h5{font-size:18px;font-weight:800;color:var(--ink);line-height:1.3;margin-top:10px}
.subscribe .field{margin-top:16px;border:1px solid var(--line);height:38px;border-radius:19px;text-align:left;padding:9px 16px;font-size:13px;color:var(--muted)}
.subscribe .btn{margin-top:12px;width:100%;font-size:13px}
.social{top:384px;left:882px;display:flex;gap:14px}
.social span{width:30px;height:30px;border-radius:50%;background:var(--white);border:1px solid var(--line)}
.copyright{top:4962px;height:52px;text-align:center;font-size:12.5px;color:var(--text);line-height:52px}
.copyright b{color:var(--ink)}
</style>
</head>
<body>

<header class="section hero">
  <div class="abs hero-art" role="img" aria-label="Illustration of a cleaner holding a spray bottle and sponge"></div>
  <div class="abs hero-plant" role="img" aria-label="Illustration of green leafy plant"></div>
  <div class="abs topbar"><span>☎ 0400 118 220 / 0330 4410</span><span>✉ kt.cleaning@kthmail.com</span></div>
  <div class="abs logo"><span class="logo-mark"></span><span class="logo-name">K&amp;T<br>HOLDINGS</span></div>
  <nav class="abs nav">
    <span class="active">Home</span><span>About ▾</span><span>Services ▾</span><span>Offers</span><span>Blog</span><span>Contact Us</span><span class="btn">Request an Estimate</span>
  </nav>
  <h1 class="abs hero-title">Spring <span>Cleaning?</span><br>Don’t Panic!</h1>
  <p class="abs hero-sub">We help clean all your needs with our various</p>
  <span class="abs btn hero-btn">Read More</span>
</header>

<section class="section goal">
  <div class="abs photo goal-photo" role="img" aria-label="Photo of a clean empty room with wooden floor and large windows"></div>
  <div class="abs goal-text">
    <h2>Our Goal is to Wow with<br>Every Clean</h2>
    <p>There are many variations of passages of Lorem Ipsum available, but the majority have suffered alteration in some form, by injected humour, or randomised words which don't look even slightly believable</p>
    <h3>Commercial Cleaning</h3>
    <p>There are many variations of passages of Lorem Ipsum available, but the majority have suffered alteration in some form, by injected humour, or randomised words which don't look even slightly believable</p>
    <h3>Building Cleaning</h3>
    <p>There are many variations of passages of Lorem Ipsum available, but the majority have suffered alteration in some form, by injected humour, or randomised words which don't look even slightly believable</p>
    <span class="btn">Book a Service</span>
  </div>
</section>

<section class="section reasons">
  <div class="abs head">
    <svg class="spark" width="34" height="26" viewBox="0 0 34 26"><path d="M20 2l2 7 7 2-7 2-2 7-2-7-7-2 7-2z" fill="#f7861e"/><circle cx="6" cy="20" r="2.5" fill="#f7861e"/></svg>
    <h2 class="title">Reasons Why People Choose Us</h2>
    <p class="lead">Perspiciatis unde omnis iste natus error sit voluptatem accusantium doloremque laudantium, totam rem aperiam, eaque ipsa</p>
  </div>
  <div class="abs features">
    <div class="feature">
      <div class="icon"><svg width="40" height="40" viewBox="0 0 40 40"><path d="M8 32l14-14 4 4-14 14z" fill="#f7861e"/><path d="M24 8l2 5 5 2-5 2-2 5-2-5-5-2 5-2z" fill="#f7861e"/></svg></div>
      <h4>Over<small>250,000 cleans</small></h4>
      <p>Our microfiber cloths, which capture dust and dirt rather than move it around, last longer than traditional cotton.</p>
    </div>
    <div class="feature">
      <div class="icon"><svg width="40" height="40" viewBox="0 0 40 40"><rect x="5" y="18" width="7" height="16" fill="#f7861e"/><path d="M14 18l6-12c3 0 4 2 3 6h10c2 0 3 2 2 4l-3 14c-1 2-2 3-4 3H14z" fill="#f7861e"/></svg></div>
      <h4>100%<small>Satisfaction</small></h4>
      <p>Our microfiber cloths, which capture dust and dirt rather than move it around, last longer than traditional cotton.</p>
    </div>
    <div class="feature">
      <div class="icon"><svg width="40" height="40" viewBox="0 0 40 40"><path d="M20 4c8 4 10 12 0 20C10 16 12 8 20 4z" fill="#f7861e"/><path d="M4 28c6-2 10 0 16 2 6-2 10-4 16-2v6H4z" fill="#f7861e"/></svg></div>
      <h4>Eco-Friendly<small>Cleaning Products</small></h4>
      <p>Our microfiber cloths, which capture dust and dirt rather than move it around, last longer than traditional cotton.</p>
    </div>
    <div class="feature">
      <div class="icon"><svg width="40" height="40" viewBox="0 0 40 40"><path d="M12 12h16l4 22H8z" fill="#f7861e"/><rect x="15" y="5" width="10" height="6" rx="2" fill="#f7861e"/><path d="M20 17v13M23 20h-4a2 2 0 000 4h2a2 2 0 010 4h-4" stroke="#fff" stroke-width="2" fill="none"/></svg></div>
      <h4>Cost<small>Effective</small></h4>
      <p>Our microfiber cloths, which capture dust and dirt rather than move it around, last longer than traditional cotton.</p>
    </div>
  </div>
</section>

<section class="section clients">
  <div class="abs quote-mark">“</div>
  <h2 class="abs">What<br>Clients Say:</h2>
  <div class="abs avatar" role="img" aria-label="Portrait photo of client"></div>
  <p class="abs quote">“Dealing with Industrel on a day-to-day basis has proved to be very easy. We make a telephone call, look at the options available, and then let them get on with the job while we concentrate on our business.</p>
  <p class="abs author">Helena M. Price</p>
</section>

<section class="section works">
  <div class="abs head">
    <svg class="spark" width="34" height="26" viewBox="0 0 34 26"><path d="M20 2l2 7 7 2-7 2-2 7-2-7-7-2 7-2z" fill="#f7861e"/><circle cx="6" cy="20" r="2.5" fill="#f7861e"/></svg>
    <h2 class="title">...easy as 1-2-3 See How Works</h2>
    <p class="lead">Perspiciatis unde omnis iste natus error sit voluptatem accusantium doloremque laudantium, totam rem aperiam, eaque ipsa</p>
  </div>
  <div class="abs step" style="left:78px"><div class="num">1</div><h4>Easy Online Scheduling</h4><p>Just s Few Clicks</p></div>
  <div class="abs step" style="left:420px"><div class="num">2</div><h4>Cleaning with Care</h4><p>and Eco-Friendly Products</p></div>
  <div class="abs step" style="left:766px"><div class="num">3</div><h4>Enjoy Cleanliness</h4><p>and Shine Around You</p></div>
  <svg class="abs connector" style="left:400px" width="90" height="12" viewBox="0 0 90 12"><path d="M0 6h84" stroke="#b9c6cf" stroke-dasharray="4 4"/><path d="M80 1l6 5-6 5" stroke="#b9c6cf" fill="none"/></svg>
  <svg class="abs connector" style="left:744px" width="90" height="12" viewBox="0 0 90 12"><path d="M0 6h84" stroke="#b9c6cf" stroke-dasharray="4 4"/><path d="M80 1l6 5-6 5" stroke="#b9c6cf" fill="none"/></svg>
</section>

<section class="section news">
  <div class="abs head">
    <svg class="spark" width="34" height="26" viewBox="0 0 34 26"><path d="M20 2l2 7 7 2-7 2-2 7-2-7-7-2 7-2z" fill="#f7861e"/><circle cx="6" cy="20" r="2.5" fill="#f7861e"/></svg>
    <h2 class="title">Latest News</h2>
    <p class="lead">Perspiciatis unde omnis iste natus error sit voluptatem accusantium doloremque laudantium, totam rem aperiam, eaque ipsa</p>
  </div>
  <article class="abs card" style="left:84px">
    <div class="photo" role="img" aria-label="Photo of gloved hands scrubbing a floor" style="background:linear-gradient(135deg,#e9e9e9,#f2c21c 60%,#9aa2a8)"></div>
    <h3>Get CleanEnergy for your (clean) home!</h3>
    <p class="date">▣ March 11, 2019</p>
    <p>Lorem Ipsum is simply dummy text of the printing and typesetting industry. Lorem Ipsum has been the industry's standard dummy text ever since the 1500s, when an unknown printer took a galley of type and scrambled it to make a type specimen book.</p>
    <span class="more">Read More</span>
  </article>
  <article class="abs card" style="left:436px">
    <div class="photo" role="img" aria-label="Photo of a cleaner vacuuming a carpet" style="background:linear-gradient(135deg,#5a4636,#a7875f 55%,#2f3a48)"></div>
    <h3>Get CleanEnergy for your (clean) home!</h3>
    <p class="date">▣ March 11, 2019</p>
    <p>Lorem Ipsum is simply dummy text of the printing and typesetting industry. Lorem Ipsum has been the industry's standard dummy text ever since the 1500s, when an unknown printer took a galley of type and scrambled it to make a type specimen book.</p>
    <span class="more">Read More</span>
  </article>
  <article class="abs card" style="left:788px">
    <div class="photo" role="img" aria-label="Photo of cleaning supplies in a bright room" style="background:linear-gradient(135deg,#d9dde0,#f6f6f4 50%,#b8c2c8)"></div>
    <h3>Get CleanEnergy for your (clean) home!</h3>
    <p class="date">▣ March 11, 2019</p>
    <p>Lorem Ipsum is simply dummy text of the printing and typesetting industry. Lorem Ipsum has been the industry's standard dummy text ever since the 1500s, when an unknown printer took a galley of type and scrambled it to make a type specimen book.</p>
    <span class="more">Read More</span>
  </article>
</section>

<section class="section offer" role="img" aria-label="Faded photo background of a cleaner at a window">
  <h2><span>25% off</span> New Client Discount!</h2>
  <p>Applied to your first invoice with a contract term of at least three months.</p>
  <p class="until">Offer valid until <span>01.06.2019</span></p>
</section>

<section class="section estimate">
  <div class="abs estimate-text">
    <h2>We Offer Free In-Home<br>Estimates, So Why Wait?</h2>
    <h4>Ready for a cleaner facility</h4>
    <p>Lorem Ipsum is simply dummy text of the printing and typesetting industry. Lorem Ipsum has been the industry's standard dummy text ever since the 1500s, when an unknown printer took a galley of type and scrambled it to make a type specimen book.</p>
    <p>Lorem Ipsum is simply dummy text of the printing and typesetting industry. Lorem Ipsum has been the industry's standard dummy text ever since the 1500s, when an unknown printer took a galley of type and scrambled it to make a type specimen book.</p>
    <span class="btn">Contacts Us</span>
  </div>
  <div class="abs tile tile-label" style="top:36px;left:612px">Residential<br>Cleaning</div>
  <div class="abs tile photo" style="top:36px;left:874px;background:linear-gradient(135deg,#f2e4d6,#e9b98f 50%,#9ab6cf)" role="img" aria-label="Photo of a woman and child cleaning together"></div>
  <div class="abs tile photo" style="top:232px;left:612px;background:linear-gradient(135deg,#f4e6da,#e2b08c 50%,#c9a27b)" role="img" aria-label="Photo of a smiling family at home"></div>
  <div class="abs tile photo" style="top:232px;left:874px;background:linear-gradient(135deg,#efe4da,#d9a782 50%,#6f5a4a)" role="img" aria-label="Photo of a family relaxing on a sofa"></div>
</section>

<footer class="section footer">
  <div class="abs col" style="top:82px;left:84px">
    <h5>About Us</h5>
    <p style="width:210px">Sed do eiusmod tempor incididunt ut labore et dolore magna aliqua. Ut enim ad minim veniam. Our microfiber cloths, which capture dust.</p>
    <div class="badges"><span class="badge"></span><span class="badge"></span></div>
    <p class="tagline">We Clean,<br>You Relax</p>
  </div>
  <div class="abs col" style="top:82px;left:348px">
    <h5>Services</h5>
    <ul><li>Corporate Cleaning</li><li>Home Cleaning</li><li>Floor Cleaning</li><li>Construction Cleaning</li><li>Move in Move Out Cleaning</li><li>Deep Cleaning</li></ul>
  </div>
  <div class="abs col" style="top:82px;left:612px">
    <h5>Useful Links</h5>
    <ul><li>Contact Us</li><li>About Us</li><li>News &amp; Articles</li><li>Terms of Use</li><li>Privacy Policy</li><li>Faq</li></ul>
  </div>
  <div class="abs subscribe">
    <svg width="30" height="22" viewBox="0 0 30 22"><rect x="1" y="1" width="28" height="20" fill="none" stroke="#f7861e" stroke-width="2"/><path d="M1 1l14 11L29 1" fill="none" stroke="#f7861e" stroke-width="2"/></svg>
    <h5>Subscribe to<br>Newsletter</h5>
    <div class="field">Email</div>
    <span class="btn">Subscribe</span>
  </div>
  <div class="abs social"><span></span><span></span><span></span><span></span></div>
</footer>

<div class="section copyright">© Copyrights 2019 <b>K&amp;T HOLDINGS CLEANING.</b> All rights reserved</div>

</body>
</html>
```